Software company needs a great powerpoint template

We need a powerpoint template for our growing company. Our software helps hospitals achieve quality via automating tedius manual tasks, performing them better, faster and easier than a person can. See our logo below and check out our website at qrn-medivault.com for more ideas/informaton. We will use this template for sales presentations, trade show demonstrations and partnership proposals.

Target Market(s)

Hospital managers & directors

Industry/Entity Type

Hospital

Contact Information for Business Card

name, title, office telephone, cell phone, email and website

Font styles to use
Sans Serif

Colors
2f74b3
33b8a4

Requirements
Must have
• use blues and greens, san serif fonts
Nice to have
• modern feel yet still somewhat converative

```html
<!DOCTYPE html>
<html lang="en">
<head>
<meta charset="utf-8">
<title>QRN Medivault – Presentation Template Overview</title>
<link rel="stylesheet" href="https://fonts.googleapis.com/css2?family=Open+Sans:wght@400;600;700&display=swap">
<style>
:root{
  --blue:#1a5ca8;
  --blue-dark:#124a8c;
  --blue-soft:#5d8fce;
  --green:#3aa935;
  --orange:#f6b756;
  --grey:#b9b9b9;
  --ink:#555;
  --ink-light:#9a9a9a;
  --stage:#e6e7e9;
  --white:#fff;
}
*{box-sizing:border-box;margin:0;padding:0}
html,body{width:1200px;height:1133px;overflow:hidden}
body{background:var(--stage);font-family:"Open Sans",Arial,sans-serif;color:var(--ink);position:relative}
.slide{position:absolute;width:388px;height:218px;background:var(--white);overflow:hidden;box-shadow:0 1px 4px rgba(0,0,0,.18)}
.c1{left:6px}.c2{left:406px}.c3{left:806px}
.r1{top:4px}.r2{top:228px}.r3{top:452px}.r4{top:676px}.r5{top:900px}
.abs{position:absolute}
.slide-title{position:absolute;left:18px;top:12px;font-size:17px;font-weight:400;color:var(--blue);padding-bottom:2px}
.slide-title::after{content:"";position:absolute;left:0;bottom:-3px;width:60px;height:1px;background:var(--green)}
.brand{position:absolute;right:12px;top:13px;font-size:9px;font-weight:700;color:var(--blue);display:flex;align-items:center;gap:3px;letter-spacing:.5px}
.brand .dot{width:6px;height:6px;border-radius:50%;background:var(--green)}
.brand.light{color:var(--white)}
.footer{position:absolute;left:0;right:0;bottom:0;height:9px;background:var(--blue);font-size:3.6px;color:var(--white);padding:2.5px 0 0 6px}
.footer::after{content:"";position:absolute;right:0;top:0;width:14px;height:9px;background:var(--green)}
.tiny{font-size:4px;line-height:5.2px;color:var(--ink-light)}
.label{font-size:5.5px;color:var(--blue)}
.icon{position:absolute;width:13px;height:13px;border-radius:50%;background:var(--blue);display:flex;align-items:center;justify-content:center}
.icon::after{content:"";width:5px;height:5px;border:1.3px solid var(--white);border-radius:50%}
.icon.green{background:var(--green)}
.icon.orange{background:var(--orange)}
.icon.grey{background:#9b9b9b}
.photo{position:absolute}
.para{font-size:4.6px;line-height:6px;color:var(--ink-light)}
.center{text-align:center}
.col5{position:absolute;top:58px;width:58px;text-align:center}
.col5 .icon{position:relative;margin:0 auto 4px}
.box4{position:absolute;top:84px;width:70px;height:92px;color:var(--white);text-align:center;padding-top:34px;font-size:4.3px;line-height:5.4px}
.box4 .icon{left:28px;top:12px;background:transparent;border:1px solid var(--white)}
.tl{position:absolute;border-radius:50%;color:var(--white);text-align:center;font-size:9px;display:flex;flex-direction:column;align-items:center;justify-content:center;line-height:9px}
.tl small{font-size:3.5px;line-height:4px}
.tbl{position:absolute;left:60px;top:50px;width:268px;height:138px;box-shadow:0 1px 5px rgba(0,0,0,.2);display:flex;background:var(--white)}
.tbl .col{flex:1;font-size:4px;color:var(--ink)}
.tbl .head{height:30px;color:var(--white);font-size:5.5px;font-weight:700;display:flex;align-items:center;padding-left:6px}
.tbl .rows{padding:16px 6px 0}
.tbl .rows div{height:7.4px}
.skill{position:absolute;left:14px;width:84px;font-size:3.6px;color:var(--blue)}
.skill .bar{height:6px;background:#d8d8d8;margin-top:1px;border-radius:1px}
.skill .bar i{display:block;height:6px;background:var(--blue);border-radius:1px}
.skill.exp{color:var(--orange)}
.skill.exp .bar i{background:var(--orange)}
.skill.g{color:var(--green)}
.skill.g .bar i{background:var(--green)}
.avatar{position:absolute;width:30px;height:30px;border-radius:50%;background:linear-gradient(#7d7d7d,#3e3e3e);border:2px solid var(--white);box-shadow:0 0 0 1px #ddd}
.person{position:absolute;width:70px;text-align:center;font-size:4.4px;color:var(--ink)}
.person b{display:block;color:var(--blue);font-weight:400;font-size:4px}
.contact-row{position:absolute;left:52px;font-size:6px;color:var(--white);display:flex;gap:8px;align-items:flex-start;line-height:7px}
.contact-row i{width:5px;height:5px;background:var(--white);border-radius:1px;margin-top:1px;flex:none}
</style>
</head>
<body>

<section class="slide c1 r1">
  <h2 class="slide-title">Our Blank Page</h2>
  <div class="brand">QRN<span class="dot"></span></div>
  <div class="footer">© 2016 QRN Medivault Systems LLC. All rights reserved.</div>
</section>

<section class="slide c2 r1">
  <h2 class="slide-title">Multiple Column Area</h2>
  <div class="brand">QRN<span class="dot"></span></div>
  <div class="col5" style="left:18px"><div class="icon"></div><div class="label">Your Text Here</div><div class="tiny">Lorem ipsum consectetur adipiscing elit.</div></div>
  <div class="col5" style="left:89px"><div class="icon"></div><div class="label">Your Text Here</div><div class="tiny">Lorem ipsum consectetur adipiscing elit.</div></div>
  <div class="col5" style="left:160px"><div class="icon"></div><div class="label">Your Text Here</div><div class="tiny">Lorem ipsum consectetur adipiscing elit.</div></div>
  <div class="col5" style="left:231px"><div class="icon"></div><div class="label">Your Text Here</div><div class="tiny">Lorem ipsum consectetur adipiscing elit.</div></div>
  <div class="col5" style="left:302px"><div class="icon"></div><div class="label">Your Text Here</div><div class="tiny">Lorem ipsum consectetur adipiscing elit.</div></div>
  <div class="abs" style="left:26px;top:119px;width:336px;height:1px;background:var(--green)"></div>
  <div class="abs" style="left:26px;top:133px;width:155px"><div class="label" style="font-size:8px">Heading Goes Here</div><p class="para">Lorem ipsum dolor sit amet, consectetur adipiscing elit, sed do eiusmod tempor incididunt ut labore et dolore magna aliqua.</p><p class="para" style="margin-top:4px">Duis aute irure dolor in reprehenderit in voluptate velit esse cillum dolore eu fugiat nulla pariatur.</p></div>
  <div class="abs" style="left:207px;top:133px;width:155px"><div class="label" style="font-size:8px">Heading Goes Here</div><p class="para">Lorem ipsum dolor sit amet, consectetur adipiscing elit, sed do eiusmod tempor incididunt ut labore et dolore magna aliqua.</p><p class="para" style="margin-top:4px">Duis aute irure dolor in reprehenderit in voluptate velit esse cillum dolore eu fugiat nulla pariatur.</p></div>
  <div class="footer">© 2016 QRN Medivault Systems LLC. All rights reserved.</div>
</section>

<section class="slide c3 r1">
  <h2 class="slide-title">Financial Graph</h2>
  <div class="brand">QRN<span class="dot"></span></div>
  <p class="para abs" style="left:18px;top:44px;width:150px">Lorem ipsum dolor sit amet, consectetur adipiscing elit, sed do eiusmod tempor incididunt ut labore et dolore magna aliqua. Ut enim minim veniam.</p>
  <p class="para abs" style="left:210px;top:44px;width:150px">Lorem ipsum dolor sit amet, consectetur adipiscing elit, sed do eiusmod tempor incididunt ut labore et dolore magna aliqua.</p>
  <svg class="abs" style="left:30px;top:80px" width="120" height="110" viewBox="0 0 120 110" aria-label="Donut chart">
    <g transform="rotate(-90 60 55)" fill="none" stroke-width="20">
      <circle cx="60" cy="55" r="38" stroke="var(--blue)" stroke-dasharray="129 240" stroke-dashoffset="0"/>
      <circle cx="60" cy="55" r="38" stroke="var(--green)" stroke-dasharray="62 240" stroke-dashoffset="-129"/>
      <circle cx="60" cy="55" r="38" stroke="var(--orange)" stroke-dasharray="19 240" stroke-dashoffset="-191"/>
      <circle cx="60" cy="55" r="38" stroke="var(--grey)" stroke-dasharray="29 240" stroke-dashoffset="-210"/>
    </g>
    <g font-size="5" fill="#fff" font-family="Open Sans,sans-serif" text-anchor="middle">
      <text x="95" y="66">54%</text><text x="26" y="74">26%</text><text x="29" y="37">8%</text><text x="46" y="23">12%</text>
    </g>
  </svg>
  <svg class="abs" style="left:196px;top:78px" width="180" height="120" viewBox="0 0 180 120" aria-label="Line chart, Series 1">
    <text x="80" y="12" font-size="5" fill="#777" font-family="Open Sans,sans-serif">Series 1</text>
    <g font-size="4" fill="#999" font-family="Open Sans,sans-serif">
      <text x="0" y="22">80</text><text x="0" y="34">70</text><text x="0" y="46">60</text><text x="0" y="58">50</text><text x="0" y="70">40</text><text x="0" y="82">30</text><text x="0" y="94">20</text><text x="0" y="106">10</text>
      <text x="20" y="116">aa</text><text x="38" y="116">ba</text><text x="56" y="116">ca</text><text x="74" y="116">da</text><text x="92" y="116">ea</text><text x="110" y="116">fa</text><text x="128" y="116">ga</text><text x="146" y="116">ha</text>
    </g>
    <polyline fill="none" stroke="var(--blue)" stroke-width="1.4" points="22,92 40,36 58,80 76,46 94,70 112,28 130,80 148,56"/>
  </svg>
  <div class="footer">© 2016 QRN Medivault Systems LLC. All rights reserved.</div>
</section>

<section class="slide c1 r2">
  <div class="photo" role="img" aria-label="Blurred office team photo in blue tint" style="inset:0 0 90px 0;background:linear-gradient(120deg,#6f9bd2,#3b74bd 60%,#2f66ae)"></div>
  <div class="brand light" style="left:50px;right:auto;top:40px;font-size:12px">QRN<span class="dot"></span></div>
  <h2 class="abs" style="left:196px;top:42px;font-size:15px;font-weight:400;color:var(--white)">Your Title Goes Here</h2>
  <p class="para abs" style="left:196px;top:64px;width:160px;color:#e3ecf7">Lorem ipsum dolor sit amet, consectetur adipiscing elit, sed do eiusmod tempor incididunt ut labore et dolore magna aliqua. Duis aute irure dolor in reprehenderit.</p>
  <div class="photo" role="img" aria-label="Photo of smiling colleagues at a meeting table" style="left:30px;top:68px;width:128px;height:104px;background:linear-gradient(135deg,#d9cfc7,#a7b4c4);border:2px solid var(--white)"></div>
  <div class="icon" style="left:176px;top:134px"></div>
  <div class="abs" style="left:196px;top:133px;width:70px"><div class="label">Your Text Here</div><div class="tiny">Lorem ipsum dolor sit amet, consectetur adipiscing.</div></div>
  <div class="icon" style="left:272px;top:134px"></div>
  <div class="abs" style="left:292px;top:133px;width:70px"><div class="label">Your Text Here</div><div class="tiny">Lorem ipsum dolor sit amet, consectetur adipiscing.</div></div>
  <div class="icon" style="left:176px;top:165px"></div>
  <div class="abs" style="left:196px;top:164px;width:70px"><div class="label">Your Text Here</div><div class="tiny">Lorem ipsum dolor sit amet, consectetur adipiscing.</div></div>
  <div class="icon" style="left:272px;top:165px"></div>
  <div class="abs" style="left:292px;top:164px;width:70px"><div class="label">Your Text Here</div><div class="tiny">Lorem ipsum dolor sit amet, consectetur adipiscing.</div></div>
  <div class="footer">© 2016 QRN Medivault Systems LLC. All rights reserved.</div>
</section>

<section class="slide c2 r2">
  <div class="photo" role="img" aria-label="Blurred laboratory background in blue tint" style="inset:0;background:linear-gradient(160deg,#6b98d0,#3c74bb 55%,#2d64aa)"></div>
  <div class="brand light" style="top:26px;right:14px;font-size:12px">QRN<span class="dot"></span></div>
  <div class="abs" style="left:146px;top:118px;width:52px;height:44px;background:var(--green);display:flex;align-items:center;justify-content:center;color:var(--white);font-weight:700;font-size:11px">QRN</div>
  <div class="abs" style="left:198px;top:118px;width:190px;height:44px;background:var(--blue);color:var(--white);padding:3px 0 0 8px">
    <div style="font-size:5.5px">Divider Page</div>
    <div style="font-size:16px;line-height:20px">Your Title Goes Here</div>
    <div style="font-size:8px;color:#cfe0f3">Your Subtitle Here</div>
  </div>
</section>

<section class="slide c3 r2">
  <div class="abs" style="left:0;right:0;top:34px;height:74px;background:#eef3fa"></div>
  <h2 class="slide-title">Our Video Area</h2>
  <div class="abs" style="left:14px;top:52px;width:150px"><div style="font-size:7px;color:var(--ink)">Heading Here</div><p class="para" style="margin-top:3px">Lorem ipsum dolor sit amet, consectetur adipiscing elit, sed do eiusmod tempor incididunt ut labore et dolore magna aliqua. Ut enim minim veniam, quis nostrud exercitation.</p></div>
  <div class="abs" style="left:165px;top:18px;width:210px;height:130px;background:#222;border-radius:5px;padding:6px">
    <div class="photo" role="img" aria-label="Video still of medical staff in a hospital laboratory" style="position:relative;width:100%;height:100%;background:linear-gradient(135deg,#e7eef3,#aebfcd)"></div>
    <div class="abs" style="left:95px;top:55px;width:20px;height:20px;border-radius:50%;background:#d62a21"></div>
  </div>
  <div class="abs" style="left:255px;top:148px;width:30px;height:14px;background:#c9c9c9"></div>
  <div class="abs" style="left:245px;top:160px;width:50px;height:3px;background:#b0b0b0;border-radius:2px"></div>
  <div class="icon" style="left:14px;top:118px"></div>
  <p class="para abs" style="left:32px;top:116px;width:120px">Lorem ipsum dolor sit amet, consectetur adipiscing elit, sed do eiusmod tempor incididunt ut labore et dolore magna aliqua.</p>
  <div class="icon" style="left:14px;top:141px"></div>
  <p class="para abs" style="left:32px;top:139px;width:120px">Lorem ipsum dolor sit amet, consectetur adipiscing elit, sed do eiusmod tempor incididunt ut labore et dolore magna aliqua.</p>
  <div class="icon" style="left:14px;top:164px"></div>
  <p class="para abs" style="left:32px;top:162px;width:120px">Lorem ipsum dolor sit amet, consectetur adipiscing elit, sed do eiusmod tempor incididunt ut labore et dolore magna aliqua.</p>
</section>

<section class="slide c1 r3">
  <h2 class="slide-title">Four Column Area</h2>
  <div class="brand">QRN<span class="dot"></span></div>
  <p class="para abs" style="left:18px;top:50px;width:350px">Lorem ipsum dolor sit amet, consectetur adipiscing elit, sed do eiusmod tempor incididunt ut labore et dolore magna aliqua. Ut enim minim veniam, quis nostrud exercitation ullamco laboris nisi ut aliquip ex ea commodo consequat.</p>
  <div class="box4" style="left:29px;background:var(--blue)"><div class="icon"></div>YOUR TEXT HERE<br>Lorem ipsum dolor sit consectetur adipiscing elit.</div>
  <div class="box4" style="left:115px;background:var(--green)"><div class="icon"></div>YOUR TEXT HERE<br>Lorem ipsum dolor sit consectetur adipiscing elit.</div>
  <div class="box4" style="left:201px;background:var(--blue)"><div class="icon"></div>YOUR TEXT HERE<br>Lorem ipsum dolor sit consectetur adipiscing elit.</div>
  <div class="box4" style="left:287px;background:var(--green)"><div class="icon"></div>YOUR TEXT HERE<br>Lorem ipsum dolor sit consectetur adipiscing elit.</div>
  <div class="footer">© 2016 QRN Medivault Systems LLC. All rights reserved.</div>
</section>

<section class="slide c2 r3">
  <h2 class="slide-title">Timeline</h2>
  <div class="brand">QRN<span class="dot"></span></div>
  <svg class="abs" style="left:0;top:0" width="388" height="218" aria-hidden="true">
    <line x1="50" y1="100" x2="330" y2="100" stroke="#ccc" stroke-width="1"/>
    <g stroke="#ccc"><line x1="100" y1="82" x2="100" y2="100"/><line x1="192" y1="82" x2="192" y2="100"/><line x1="284" y1="82" x2="284" y2="100"/><line x1="146" y1="100" x2="146" y2="116"/><line x1="238" y1="100" x2="238" y2="116"/></g>
  </svg>
  <div class="tl" style="left:32px;top:82px;width:38px;height:38px;background:var(--blue)">2011<small>Your Text<br>Goes Here</small></div>
  <div class="tl" style="left:81px;top:48px;width:38px;height:38px;background:var(--green)">2012<small>Your Text<br>Goes Here</small></div>
  <div class="tl" style="left:127px;top:112px;width:38px;height:38px;background:var(--orange)">2013<small>Your Text<br>Goes Here</small></div>
  <div class="tl" style="left:173px;top:48px;width:38px;height:38px;background:var(--blue)">2014<small>Your Text<br>Goes Here</small></div>
  <div class="tl" style="left:219px;top:112px;width:38px;height:38px;background:var(--orange)">2015<small>Your Text<br>Goes Here</small></div>
  <div class="tl" style="left:265px;top:48px;width:38px;height:38px;background:var(--green)">2016<small>Your Text<br>Goes Here</small></div>
  <div class="tl" style="left:312px;top:82px;width:38px;height:38px;background:var(--blue)">2017<small>Your Text<br>Goes Here</small></div>
  <div class="abs" style="left:270px;top:138px;width:100px"><div class="label">Your Text Goes Here</div><div class="tiny">Lorem ipsum dolor sit amet, consectetur adipiscing elit, sed do eiusmod tempor.</div></div>
  <div class="abs" style="left:18px;top:172px;width:150px"><div class="label">Your Text Goes Here</div><div class="tiny">Lorem ipsum dolor sit amet, consectetur adipiscing elit, sed do eiusmod tempor incididunt ut labore.</div></div>
  <div class="footer">© 2016 QRN Medivault Systems LLC. All rights reserved.</div>
</section>

<section class="slide c3 r3">
  <h2 class="slide-title">Workflow Area</h2>
  <div class="brand">QRN<span class="dot"></span></div>
  <p class="para abs" style="left:28px;top:50px;width:334px">Lorem ipsum dolor sit amet, consectetur adipiscing elit, sed do eiusmod tempor incididunt ut labore et dolore magna aliqua. Ut enim minim veniam, quis nostrud exercitation ullamco laboris nisi ut aliquip ex ea commodo.</p>
  <svg class="abs" style="left:0;top:0" width="388" height="218" aria-label="Five-step workflow">
    <path d="M36 142 A32 32 0 0 1 100 142 A32 32 0 0 0 164 142 A32 32 0 0 1 228 142 A32 32 0 0 0 292 142 A32 32 0 0 1 356 142" fill="none" stroke="var(--blue)" stroke-width="13"/>
    <g fill="var(--blue)"><circle cx="68" cy="124" r="6"/><circle cx="196" cy="124" r="6"/><circle cx="324" cy="124" r="6"/></g>
    <g fill="var(--green)"><circle cx="132" cy="160" r="6"/><circle cx="260" cy="160" r="6"/></g>
    <g fill="#fff" font-size="5" text-anchor="middle" font-family="Open Sans,sans-serif"><text x="68" y="126">1</text><text x="132" y="162">2</text><text x="196" y="126">3</text><text x="260" y="162">4</text><text x="324" y="126">5</text></g>
  </svg>
  <div class="abs center" style="left:40px;top:137px;width:56px"><div class="label" style="color:var(--blue-dark)">Data 1</div><div class="tiny">Lorem ipsum dolor sit amet, consectetur adipiscing.</div></div>
  <div class="abs center" style="left:104px;top:83px;width:56px"><div class="label" style="color:var(--green)">Data 2</div><div class="tiny">Lorem ipsum dolor sit amet, consectetur adipiscing.</div></div>
  <div class="abs center" style="left:168px;top:137px;width:56px"><div class="label" style="color:var(--blue-dark)">Data 3</div><div class="tiny">Lorem ipsum dolor sit amet, consectetur adipiscing.</div></div>
  <div class="abs center" style="left:232px;top:83px;width:56px"><div class="label" style="color:var(--green)">Data 4</div><div class="tiny">Lorem ipsum dolor sit amet, consectetur adipiscing.</div></div>
  <div class="abs center" style="left:296px;top:137px;width:56px"><div class="label" style="color:var(--blue-dark)">Data 5</div><div class="tiny">Lorem ipsum dolor sit amet, consectetur adipiscing.</div></div>
  <div class="footer">© 2016 QRN Medivault Systems LLC. All rights reserved.</div>
</section>

<section class="slide c1 r4">
  <h2 class="slide-title">Bullet &amp; Chart Area</h2>
  <div class="brand">QRN<span class="dot"></span></div>
  <svg class="abs" style="left:14px;top:48px" width="160" height="130" aria-label="Clustered bar chart">
    <g font-size="3.6" fill="#888" font-family="Open Sans,sans-serif"><text x="0" y="22">Category 4</text><text x="0" y="50">Category 3</text><text x="0" y="78">Category 2</text><text x="0" y="106">Category 1</text></g>
    <g>
      <rect x="50" y="14" width="100" height="4" fill="var(--orange)"/><rect x="50" y="19" width="60" height="4" fill="var(--green)"/><rect x="50" y="24" width="88" height="4" fill="var(--blue)"/>
      <rect x="50" y="42" width="62" height="4" fill="var(--orange)"/><rect x="50" y="47" width="38" height="4" fill="var(--green)"/><rect x="50" y="52" width="72" height="4" fill="var(--blue)"/>
      <rect x="50" y="70" width="40" height="4" fill="var(--orange)"/><rect x="50" y="75" width="92" height="4" fill="var(--green)"/><rect x="50" y="80" width="60" height="4" fill="var(--blue)"/>
      <rect x="50" y="98" width="45" height="4" fill="var(--orange)"/><rect x="50" y="103" width="28" height="4" fill="var(--green)"/><rect x="50" y="108" width="90" height="4" fill="var(--blue)"/>
    </g>
    <g font-size="3.4" fill="#888" font-family="Open Sans,sans-serif"><rect x="60" y="123" width="3" height="3" fill="var(--orange)"/><text x="65" y="126">Series 3</text><rect x="86" y="123" width="3" height="3" fill="var(--green)"/><text x="91" y="126">Series 2</text><rect x="112" y="123" width="3" height="3" fill="var(--blue)"/><text x="117" y="126">Series 1</text></g>
  </svg>
  <div class="icon" style="left:200px;top:54px"></div><div class="abs" style="left:222px;top:52px;width:120px"><div class="label">Category One</div><div class="tiny">Lorem ipsum dolor sit amet, consectetur adipiscing elit, sed do eiusmod.</div></div>
  <div class="icon green" style="left:200px;top:84px"></div><div class="abs" style="left:222px;top:82px;width:120px"><div class="label" style="color:var(--green)">Category Two</div><div class="tiny">Lorem ipsum dolor sit amet, consectetur adipiscing elit, sed do eiusmod.</div></div>
  <div class="icon" style="left:200px;top:114px"></div><div class="abs" style="left:222px;top:112px;width:120px"><div class="label">Category Three</div><div class="tiny">Lorem ipsum dolor sit amet, consectetur adipiscing elit, sed do eiusmod.</div></div>
  <div class="icon green" style="left:200px;top:144px"></div><div class="abs" style="left:222px;top:142px;width:120px"><div class="label" style="color:var(--green)">Category Four</div><div class="tiny">Lorem ipsum dolor sit amet, consectetur adipiscing elit, sed do eiusmod.</div></div>
  <div class="footer">© 2016 QRN Medivault Systems LLC. All rights reserved.</div>
</section>

<section class="slide c2 r4">
  <h2 class="slide-title">Table Area</h2>
  <div class="brand">QRN<span class="dot"></span></div>
  <div class="tbl">
    <div class="col" style="flex:1.35"><div class="head" style="background:var(--blue)">Description</div>
      <div class="rows"><div>Description 1</div><div>Description 2</div><div>Description 3</div><div>Description 4</div><div>Description 5</div><div>Description 6</div><div>Description 7</div><div>Description 8</div></div></div>
    <div class="col center" style="border-left:1px solid #eee"><div class="head" style="background:var(--orange);justify-content:center;padding:0">Column 1</div>
      <div class="rows"><div>•</div><div>•</div><div>•</div><div>•</div><div>Text Column 1</div><div>•</div><div>Text Column 1</div><div>•</div></div></div>
    <div class="col center" style="border-left:1px solid #eee"><div class="head" style="background:var(--green);justify-content:center;padding:0">Column 2</div>
      <div class="rows"><div>•</div><div>•</div><div>•</div><div>•</div><div>Text Column 2</div><div>•</div><div>Text Column 2</div><div>•</div></div></div>
  </div>
  <div class="footer">© 2016 QRN Medivault Systems LLC. All rights reserved.</div>
</section>

<section class="slide c3 r4">
  <h2 class="slide-title">Bullet &amp; Chart Area</h2>
  <div class="brand">QRN<span class="dot"></span></div>
  <div class="icon" style="left:38px;top:60px"></div><div class="abs" style="left:60px;top:58px;width:110px"><div class="label">Your Text Here</div><div class="tiny">Lorem ipsum dolor sit amet, consectetur adipiscing elit, sed do eiusmod.</div></div>
  <div class="icon green" style="left:38px;top:91px"></div><div class="abs" style="left:60px;top:89px;width:110px"><div class="label" style="color:var(--green)">Your Text Here</div><div class="tiny">Lorem ipsum dolor sit amet, consectetur adipiscing elit, sed do eiusmod.</div></div>
  <div class="icon orange" style="left:38px;top:122px"></div><div class="abs" style="left:60px;top:120px;width:110px"><div class="label" style="color:var(--orange)">Your Text Here</div><div class="tiny">Lorem ipsum dolor sit amet, consectetur adipiscing elit, sed do eiusmod.</div></div>
  <div class="icon grey" style="left:38px;top:153px"></div><div class="abs" style="left:60px;top:151px;width:110px"><div class="label" style="color:#888">Your Text Here</div><div class="tiny">Lorem ipsum dolor sit amet, consectetur adipiscing elit, sed do eiusmod.</div></div>
  <svg class="abs" style="left:196px;top:50px" width="180" height="140" aria-label="Quarterly donut chart">
    <g transform="rotate(-90 80 66)" fill="none" stroke-width="10">
      <circle cx="80" cy="66" r="38" stroke="var(--blue)" stroke-dasharray="130 239"/>
      <circle cx="80" cy="66" r="38" stroke="var(--green)" stroke-dasharray="54 239" stroke-dashoffset="-130"/>
      <circle cx="80" cy="66" r="38" stroke="var(--orange)" stroke-dasharray="33 239" stroke-dashoffset="-184"/>
      <circle cx="80" cy="66" r="38" stroke="var(--grey)" stroke-dasharray="22 239" stroke-dashoffset="-217"/>
    </g>
    <g fill="#9b9b9b"><rect x="70" y="62" width="4" height="10"/><rect x="76" y="56" width="4" height="16"/><rect x="82" y="52" width="4" height="20"/><rect x="88" y="58" width="4" height="14"/><rect x="67" y="72" width="28" height="1.5"/></g>
    <g font-size="11" font-family="Open Sans,sans-serif"><text x="62" y="16" fill="#9b9b9b">10%</text><text x="18" y="38" fill="var(--orange)">15%</text><text x="125" y="71" fill="var(--blue)">60%</text><text x="22" y="106" fill="var(--green)">25%</text></g>
    <g font-size="3.5" fill="#888" font-family="Open Sans,sans-serif"><rect x="52" y="124" width="3" height="3" fill="var(--blue)"/><text x="57" y="127">1st Qtr</text><rect x="70" y="124" width="3" height="3" fill="var(--green)"/><text x="75" y="127">2nd Qtr</text><rect x="88" y="124" width="3" height="3" fill="var(--orange)"/><text x="93" y="127">3rd Qtr</text><rect x="106" y="124" width="3" height="3" fill="var(--grey)"/><text x="111" y="127">4th Qtr</text></g>
  </svg>
  <div class="footer">© 2016 QRN Medivault Systems LLC. All rights reserved.</div>
</section>

<section class="slide c1 r5">
  <div class="abs" style="left:16px;top:24px;font-size:12px;color:var(--blue)">Technology</div>
  <div class="skill" style="top:42px">Clinical Workflow Automation<div class="bar"><i style="width:100%"></i></div></div>
  <div class="skill" style="top:60px">Records Sync<div class="bar"><i style="width:100%"></i></div></div>
  <div class="skill" style="top:78px">Audit Engine<div class="bar"><i style="width:80%"></i></div></div>
  <div class="abs" style="left:16px;top:110px;font-size:12px;color:var(--orange)">Experience</div>
  <div class="skill exp" style="top:128px">UX Designer<div class="bar"><i style="width:100%"></i></div></div>
  <div class="skill exp" style="top:146px">Product Lead<div class="bar"><i style="width:100%"></i></div></div>
  <div class="skill exp" style="top:164px">Systems Engineer<div class="bar"><i style="width:100%"></i></div></div>
  <div class="photo" role="img" aria-label="Photo of a smiling businessman in front of his team" style="left:116px;top:0;width:158px;height:209px;background:linear-gradient(160deg,#d8dde3,#8d97a3 60%,#4b5560)"></div>
  <div class="abs" style="left:116px;top:148px;width:158px;height:50px;background:rgba(26,92,168,.85);color:var(--white);font-size:16px;display:flex;align-items:center;justify-content:center">Our Skills</div>
  <div class="brand" style="top:16px">QRN<span class="dot"></span></div>
  <div class="abs" style="left:290px;top:52px;font-size:12px;color:var(--green)">Experience</div>
  <div class="skill g" style="left:290px;top:74px">Care Logic LTD<div class="bar"><i style="width:100%"></i></div></div>
  <div class="skill g" style="left:290px;top:94px">Ward Soft &amp; Tools<div class="bar"><i style="width:90%"></i></div></div>
  <div class="skill g" style="left:290px;top:114px">Nordline Health<div class="bar"><i style="width:85%"></i></div></div>
  <div class="skill g" style="left:290px;top:134px">Lumen Metrics<div class="bar"><i style="width:55%"></i></div></div>
  <div class="footer">© 2016 QRN Medivault Systems LLC. All rights reserved.</div>
</section>

<section class="slide c2 r5">
  <div class="photo" role="img" aria-label="Photo of a business team standing together" style="left:0;top:0;width:128px;height:209px;background:linear-gradient(160deg,#cfd4da,#7b8591 55%,#2f353d)"></div>
  <div class="abs" style="left:0;top:148px;width:128px;height:50px;background:rgba(26,92,168,.88);color:var(--white);font-size:14px;display:flex;align-items:center;justify-content:center">Meet Our Team</div>
  <div class="brand" style="top:16px">QRN<span class="dot"></span></div>
  <div class="avatar" role="img" aria-label="Portrait of company president" style="left:134px;top:16px;width:40px;height:40px"></div>
  <div class="abs" style="left:181px;top:22px;font-size:7px;color:var(--ink)">James Smith<div style="color:var(--blue);font-size:6px">President &amp; CEO</div><div class="tiny">emailaddress@email.com</div></div>
  <div class="avatar" role="img" aria-label="Portrait of VP Marketing" style="left:192px;top:64px"></div>
  <div class="person" style="left:172px;top:97px">John Smith<b>VP Marketing</b><span class="tiny">email@email.com</span></div>
  <div class="avatar" role="img" aria-label="Portrait of VP Finance" style="left:290px;top:64px"></div>
  <div class="person" style="left:270px;top:97px">George Smith<b>VP Finance</b><span class="tiny">email@email.com</span></div>
  <div class="avatar" role="img" aria-label="Portrait of VP Business Development" style="left:192px;top:135px"></div>
  <div class="person" style="left:172px;top:168px">Mark Smith<b>VP of Business Development</b><span class="tiny">email@email.com</span></div>
  <div class="avatar" role="img" aria-label="Portrait of marketing manager" style="left:290px;top:135px"></div>
  <div class="person" style="left:270px;top:168px">Jane Smith<b>Manager Marketing</b><span class="tiny">email@email.com</span></div>
  <div class="footer">© 2016 QRN Medivault Systems LLC. All rights reserved.</div>
</section>

<section class="slide c3 r5">
  <div class="photo" role="img" aria-label="Blurred hospital background in blue tint" style="inset:0;background:linear-gradient(150deg,#8cb0dc,#5a8bc8 50%,#3e73b8)"></div>
  <div class="abs" style="left:36px;top:0;width:130px;height:218px;background:var(--blue)"></div>
  <div class="brand light" style="left:56px;right:auto;top:26px;font-size:12px">QRN<span class="dot"></span></div>
  <div class="abs" style="left:52px;top:70px;font-size:16px;color:var(--white)">Our Contact</div>
  <div class="contact-row" style="top:106px"><i></i><span>123 Street Road<br>City 12345</span></div>
  <div class="contact-row" style="top:128px"><i></i><span>(123) 456-7890</span></div>
  <div class="contact-row" style="top:145px"><i></i><span>emailaddress@email.com</span></div>
  <div class="contact-row" style="top:162px"><i></i><span>www.qrn-medivault.com</span></div>
  <div class="abs" style="left:36px;top:194px;width:130px;height:24px;background:var(--green);display:flex;justify-content:center;align-items:center;gap:6px">
    <span style="width:9px;height:9px;border-radius:50%;background:var(--white)"></span><span style="width:9px;height:9px;border-radius:50%;background:var(--white)"></span><span style="width:9px;height:9px;border-radius:50%;background:var(--white)"></span>
  </div>
  <div class="abs center" style="left:210px;top:118px;width:150px;color:var(--white)">
    <div style="font-size:16px;font-weight:700">THANK YOU</div>
    <div style="font-size:6px">For Your Precious Time</div>
    <div style="font-size:5px;margin-top:4px;color:#e4edf8">Stop by our office or give us a call<br>We would love to hear from you.</div>
  </div>
</section>

</body>
</html>
```